Web Design Project Bright Lane

I am needing a website for a theatre called Bright Lane Stage School (blstageschool.com) which has already been purchsed from web nook. (Let me know if you need any other info on that.)We need a website that is professional looking and easy to access. Attached is the logo as well as the business card design. I think it would be nice to have the same type of design that’s on the business card but I am definitely open to other creative ideas. I need the website to be in a format where I can edit it in the future when I need to add classes and events to it. Also, some other things I need are I need are a…
A homepage. On the homepage we would like the motto, “Rise to the spotlight.” Also, the mission statement,
Bright Lane Stage School strives to help students achieve excellence in performance, while building self-confidence and creativity. The Bright Lane Stage School has created a fun and safe environment, where students can learn, acquire new skills, and explore their potential through musical theatre. Students not only have the freedom to, but are encouraged to embrace who they are and can lose their fear of judgment from others.
Class Registration Page for the classes- (As well as a quick fund option for each if that is possible)
4-6 Musical Theatre
Tuesday’s 4:00PM-5:00PM
January 6th – February 24th
8 Weeks
Cost $160
Curriculum: Moss Kite
Class info: In MT 4-6 your students will learn the basics of singing, dancing, and acting. A lesson of theatre terminology or technique will be taught each week as well as working on the show that will be performed at the end of the 8 weeks semester.

6-9 Musical Theatre
Tuesday’s 5:15PM-6:45PM
January 6th- February 24th
8 Weeks
Cost: $200
Curriculum: Delia
Class info: In MT 6-9 your students will learn the basics of singing, dancing, and acting. A lesson of theatre terminology or technique will be taught each week as well as working on the show that will be performed at the end of the 8 weeks semester.
9-12 Musical Theatre
Wednesday’s 5:00-7:00PM
8 Weeks
Cost: $240
Curriculum: Gilded
Class info: In MT 9-12 your students will learn intermediate levels of singing, dancing, and acting. A lesson of theatre terminology or technique will be taught each week as well as working on the show that will be performed at the end of the 8 weeks semester.

About- (Include headshot that is attached)
A native Coloradan, Marisol is an actress, director, teacher, and wife. She was a Dean’s List graduate of Northvale College in Florida, she holds a B.S. degree in Theatre. Her Capstone Project involved writing, producing, directing, and starring in a 60-minute one-woman musical which was noted by the Chairman of Theatre as setting new standard for the NVC project. Initially attending Harrow Ridge College, Marisol was one of nine students representing HR at the Upper Plains Drama Festival. Marisol has also been a senior theatre director at the Willowmere Youth Playhouse for 4 years, where she directed fall, spring, and summer classes for ages 4-19. Her experience includes directing the main stage production, Quill Tr., assistant director for, Nobody Minds Old Tobias Grey, and stage management for Der Wandelstern.

Contact us
Phone: 555-214-7390
Email: blstageschoolhub.com

Also, I do not have any photos of students yet so it's ok if their aren't many pictures because I intend on adding some when things get going, so if it's simple that's great. Also, if you find any musical theatre pictures that don't include faces, are just bodies or feet, that would work as well.
Updates

The web address needs to be blstageschool.com. I have already purchased the domain name from WebNook. Let me know if there are any steps I might be missing or any other info I need to provide. Also, I need to be able to edit the website in the future but I'm not sure which format is best for that.

Target Market(s)

Theatre parents and students

Industry/Entity Type

Building

Requirements
Must have
• Stated above.

```html
<!DOCTYPE html>
<html lang="en">
<head>
<meta charset="utf-8">
<title>Bright Lane Stage School</title>
<link rel="stylesheet" href="https://fonts.googleapis.com/css2?family=Lato:ital,wght@0,400;0,700;1,400&family=Fondamento:ital@1&display=swap">
<style>
  :root {
    --accent: #8b0206;
    --sky-top: #ebbde8;
    --sky-mid: #f7e6f5;
    --sky-bottom: #ffffff;
    --floor-top: #b08a60;
    --floor-bottom: #c6a47b;
    --ink: #1e1e1e;
    --brand-ink: #3a3a3a;
    --motto: #8b0a12;
    --nav-text: #ffffff;
    --light-fill: #2a2a2a;
  }
  * { margin: 0; padding: 0; box-sizing: border-box; }
  html, body { width: 1200px; height: 960px; overflow: hidden; }
  body { font-family: "Lato", Arial, sans-serif; color: var(--ink); }

  .stage {
    position: relative;
    width: 1200px;
    height: 960px;
    overflow: hidden;
  }
  .stage__backdrop {
    position: absolute; inset: 0;
    background: linear-gradient(180deg,
      var(--sky-top) 0%,
      var(--sky-mid) 45%,
      var(--sky-bottom) 74%,
      var(--floor-top) 83%,
      var(--floor-bottom) 100%);
  }

  .brand {
    position: absolute; left: 0; top: 200px; width: 1200px;
    text-align: center;
    font-weight: 400;
    font-size: 36px;
    line-height: 1.2;
    color: var(--brand-ink);
  }
  .motto {
    position: absolute; left: 0; top: 310px; width: 1200px;
    text-align: center;
    font-family: "Fondamento", Georgia, serif;
    font-style: italic;
    font-size: 33px;
    color: var(--motto);
  }

  .main-nav {
    position: absolute; left: 205px; top: 393px; width: 789px; height: 43px;
    background: var(--accent);
    border-radius: 4px;
  }
  .main-nav__link {
    position: absolute; top: 0; line-height: 43px;
    transform: translateX(-50%);
    color: var(--nav-text);
    font-weight: 700;
    font-size: 21px;
    text-decoration: none;
    white-space: nowrap;
  }

  .mission { position: absolute; left: 205px; top: 469px; width: 516px; }
  .mission__title { font-style: italic; font-weight: 400; font-size: 25px; margin-bottom: 24px; }
  .mission__text { font-size: 14.3px; line-height: 30px; text-align: justify; }

  .spotlight {
    position: absolute; left: 810px; top: 480px; width: 260px; height: 435px;
    background: radial-gradient(ellipse at 50% 20%, #4a4a4a 0%, var(--light-fill) 55%, rgba(42,42,42,0.15) 100%);
    border-radius: 6px;
  }

  .contact {
    position: absolute; left: 205px; top: 788px;
    font-style: normal;
    color: #ffffff; font-size: 21px; line-height: 35px;
  }
</style>
</head>
<body>
<main class="stage">
  <div class="stage__backdrop" role="img" aria-label="Stage scene with red curtains drawn open over a wooden floor"></div>

  <div class="brand">Bright Lane<br>Stage School</div>
  <p class="motto">Rise To The Spotlight</p>

  <nav class="main-nav">
    <a class="main-nav__link" href="#" style="left:82px">Home</a>
    <a class="main-nav__link" href="#" style="left:259px">About Us</a>
    <a class="main-nav__link" href="#" style="left:467px">Registration</a>
    <a class="main-nav__link" href="#" style="left:680px">Contact Us</a>
  </nav>

  <section class="mission">
    <h2 class="mission__title">Mission Statment</h2>
    <p class="mission__text">Bright Lane Stage School strives to help students achieve excellence in performance, while building self-confidence and creativity. The Bright Lane Stage School has created a fun and safe environment, where students can learn, acquire new skills, and explore their potential through musical theatre. Students not only have the freedom to, but are encouraged to embrace who they are and can lose their fear of judgment from others.</p>
  </section>

  <div class="spotlight" role="img" aria-label="Studio spotlight on a black tripod stand"></div>

  <address class="contact">
    Contact us<br>
    Phone: 555-214-7390<br>
    Email: blstageschoolhub.com
  </address>
</main>
</body>
</html>
```